Mental Health Awareness License Plates

Below is the sample format I will need. That of a plain license plate w/o frame
*refer to image with name Licence wo Frame*
Delete Frame
Replace QR Code with “MO”
Replace 2025 sticker with “ YR
Use License Plate font (attached)
On Ribbon, keep the green background
The California front leg, needs to be gradated like a sunset and retain shape of CA
Palm trees sharpened
I need the files in a format that can be used on a website, printed or made into a poster.
One file that reads SAMPLE, one version that reads “NEWPLA8”d
The finished product should look like a license plate as shown in the example
*refer to image name finished product*
I want to clarify what we are looking for. The license plate design has been approved by the state, but we need a high res version of it in multiple file formats. The most important change we are looking for is to the ribbon. The palm trees against the sunset are fuzzy, we need those placed in front of an sunset on the front leg of the ribbon. The rear leg needs to remain green (mental health color). I hope this help clarify our design need.

```html
<!DOCTYPE html>
<html lang="en">
<head>
<meta charset="UTF-8">
<title>Mental Health Awareness License Plates</title>
<link rel="stylesheet" href="https://fonts.googleapis.com/css2?family=Oswald:wght@500&family=Montserrat:wght@500;700&display=swap">
<style>
  :root {
    --canvas-bg: #e0e1e1;
    --plate-mint: #c8f5e4;
    --plate-edge: #b6e8d5;
    --plate-inner: #d4f9ec;
    --state-red: #d8141c;
    --box-red: #d6333a;
    --ink-navy: #324a6a;
    --hole-fill: #ffffff;
    --hole-ring: #8a9a94;
    --ribbon-green: #5fae2e;
    --sunset-orange: #d98a3a;
    --sunset-yellow: #f2d23a;
  }
  * { margin: 0; padding: 0; box-sizing: border-box; }
  html, body {
    width: 1200px; height: 750px; overflow: hidden;
    background: var(--canvas-bg);
  }
  .canvas { position: relative; width: 1200px; height: 750px; }

  .plate {
    position: absolute; left: 296px; width: 608px; height: 290px;
    background: var(--plate-mint);
    border-radius: 18px;
    border: 3px solid var(--plate-edge);
    box-shadow: 0 8px 10px rgba(0,0,0,0.28), inset 0 0 0 10px var(--plate-inner);
  }
  .plate--sample { top: 52px; }
  .plate--custom { top: 402px; }

  .sticker-box {
    position: absolute; top: 13px; width: 82px; height: 44px;
    border: 1.5px solid var(--box-red);
    color: var(--box-red);
    font: 500 12px/1 "Montserrat", sans-serif;
    letter-spacing: 1px;
    display: flex; flex-direction: column; align-items: center; justify-content: center; gap: 4px;
  }
  .sticker-box--month { left: 13px; }
  .sticker-box--year { right: 13px; }
  .sticker-box__bar { width: 22px; height: 6px; background: var(--box-red); }

  .state-name {
    position: absolute; left: 0; right: 0; top: 18px;
    text-align: center;
    font: 700 56px/1 "Montserrat", sans-serif;
    color: var(--state-red);
  }

  .bolt-hole {
    position: absolute; width: 14px; height: 14px; border-radius: 50%;
    background: var(--hole-fill); border: 1.5px solid var(--hole-ring);
  }
  .bolt-hole--tl { left: 121px; top: 13px; }
  .bolt-hole--tr { left: 470px; top: 13px; }
  .bolt-hole--bl { left: 121px; top: 259px; }
  .bolt-hole--br { left: 470px; top: 259px; }

  .ribbon-art {
    position: absolute; left: 16px; top: 88px; width: 92px; height: 158px;
    border-radius: 40px 40px 10px 10px;
    background: linear-gradient(120deg, var(--ribbon-green) 0%, var(--ribbon-green) 30%, var(--sunset-orange) 45%, var(--sunset-yellow) 100%);
  }

  .plate-number {
    position: absolute; left: 128px; top: 108px; width: 432px; height: 126px;
  }
  .plate-number text {
    font-family: "Oswald", sans-serif; font-weight: 500;
    fill: var(--ink-navy);
  }

  .tagline {
    position: absolute; left: 0; right: 0; top: 257px;
    text-align: center;
    font: 700 17px/1 "Montserrat", sans-serif;
    letter-spacing: 1.9px;
    color: var(--ink-navy);
  }
</style>
</head>
<body>
<main class="canvas">

  <section class="plate plate--sample">
    <div class="sticker-box sticker-box--month">MO</div>
    <div class="sticker-box sticker-box--year">YR<span class="sticker-box__bar"></span></div>
    <span class="bolt-hole bolt-hole--tl"></span>
    <span class="bolt-hole bolt-hole--tr"></span>
    <span class="bolt-hole bolt-hole--bl"></span>
    <span class="bolt-hole bolt-hole--br"></span>
    <h2 class="state-name">California</h2>
    <div class="ribbon-art" role="img" aria-label="Awareness ribbon with a green rear leg and a California-shaped front leg showing palm trees against a sunset"></div>
    <svg class="plate-number" viewBox="0 0 432 126">
      <text x="0" y="122" font-size="164" textLength="432" lengthAdjust="spacingAndGlyphs">SAMPLE</text>
    </svg>
    <p class="tagline">MENTAL HEALTH AWARENESS</p>
  </section>

  <section class="plate plate--custom">
    <div class="sticker-box sticker-box--month">MO</div>
    <div class="sticker-box sticker-box--year">YR<span class="sticker-box__bar"></span></div>
    <span class="bolt-hole bolt-hole--tl"></span>
    <span class="bolt-hole bolt-hole--tr"></span>
    <span class="bolt-hole bolt-hole--bl"></span>
    <span class="bolt-hole bolt-hole--br"></span>
    <h2 class="state-name">California</h2>
    <div class="ribbon-art" role="img" aria-label="Awareness ribbon with a green rear leg and a California-shaped front leg showing palm trees against a sunset"></div>
    <svg class="plate-number" viewBox="0 0 432 126">
      <text x="0" y="122" font-size="164" textLength="432" lengthAdjust="spacingAndGlyphs">NEWPLA8</text>
    </svg>
    <p class="tagline">MENTAL HEALTH AWARENESS</p>
  </section>

</main>
</body>
</html>
```